Web Design for non-profit, Nautical themed

We are developing a web design for a non-profit organization. They are:

a non-profit 501©3 educational and service organization, grounded in the recognition that active engagement of the arts through can be an entry into growth and transformation. Our purpose is to develop and offer events that support this creative process bringing outstanding presenters to our town.

They are located in a beautiful coastal town and the client would like a "nautical" theme. This would include

- color palette of blue, green, possibly brown/beige, and possibly some deep red colors as accents. There is a file attached with some color palette ideas, but you don't have to choose from colors here.

- soothing, calm, clean professional look

- something in the background image that would indicate the four directions. This could be a compass or something similar.

- the client really likes this website:
http://www.brambleharbourguild.org/

Please see attached for:

- a basic sketch that shows the overall layout that we desire. Feel free to modify this slightly but not too much. File name is 01-sketch.psd

- placeholder content that can be used throughout your design

You can also use any of the stock photos found here:
http://www.pixelquarryimages.com/search/lightbox/48207365#a9k2d71

Target Market(s)

Mainly white American women who are in their 40s or older. Professional, affluent, highly educated.

Industry/Entity Type

Nautical

Requirements
Must have
• - sidebar with event information. Each event should include date, headshot, title, brief description and a "Register" and "Read more" link. We don't have any real headshots so use ones from Internet for now.

- use the attached 01-sketch.psd file as your starting point.

```html
<!DOCTYPE html>
<html lang="en">
<head>
<meta charset="utf-8">
<title>Tidewater Dialogues</title>
<link href="https://fonts.googleapis.com/css2?family=Arimo:wght@400;700&family=Oswald:wght@500&family=PT+Sans+Narrow:wght@400;700&display=swap" rel="stylesheet">
<style>
:root{
  --navy:#063768;
  --white:#ffffff;
  --band:#c6dcec;
  --panel:#e4ecf5;
  --ink:#0f3e78;
  --text:#111111;
  --grey:#555555;
  --accent:#c0480e;
  --gold:#e0a050;
  --line:#d7d7d7;
}
*{box-sizing:border-box;margin:0;padding:0}
html,body{width:1200px;height:967px;overflow:hidden}
body{background:var(--navy);font-family:"Arimo",Arial,sans-serif;position:relative;color:var(--text)}
.abs{position:absolute}
.nav{left:202px;top:0;width:795px;height:44px;background:var(--white);display:flex;align-items:center;justify-content:space-between;padding:0 16px 0 8px}
.nav a{font-size:13px;font-weight:700;color:var(--grey);text-decoration:none;padding:4px 7px}
.nav a.active{background:var(--accent);color:var(--white)}
.masthead{left:202px;top:53px;width:795px;height:99px;background:var(--white);display:flex;align-items:center;padding-left:12px}
.brand-mark{width:60px;height:60px;background:#555;margin-right:14px}
.brand-name{font-size:34px;color:#444;letter-spacing:.5px}
.sidebar{left:203px;top:163px;width:253px;height:678px;background:var(--white)}
.band{background:var(--band);height:31px;font-family:"Oswald",sans-serif;font-size:17px;color:#222;padding:3px 11px;text-transform:uppercase;letter-spacing:-.2px}
.socials{display:flex;gap:10px;padding:13px 15px;height:60px}
.sq{width:27px;height:27px;border-radius:4px}
.fb{background:#3b5a9a}.yt{background:#c9c2bc}.tw{background:#5cb8d0}
.mail{display:flex;gap:8px;padding:19px 15px;height:62px}
.mail .field{width:174px;height:25px;border:1px solid #e3d6c8}
.mail .join{width:45px;height:25px;background:var(--accent);color:var(--white);font-family:"Oswald",sans-serif;font-size:12px;letter-spacing:2px;display:flex;align-items:center;justify-content:center}
.event{position:absolute;left:15px;width:226px;font-size:9.5px;line-height:12.2px}
.headshot{position:absolute;left:0;width:90px;height:114px;border:1px solid var(--ink);padding:2px}
.headshot div{width:100%;height:100%}
.meta{position:absolute;left:108px;top:0;font-weight:700;color:var(--ink);font-size:10px;line-height:17px}
.lead{position:absolute;left:108px;width:118px;text-align:justify}
.rest{position:absolute;left:0;width:226px;text-align:justify}
.main{left:472px;top:163px;width:525px;height:676px;background:var(--white)}
.slide{left:486px;top:176px;width:497px;height:312px;border:4px solid #ccc;background:linear-gradient(180deg,#5a64b6 0%,#7b84c8 45%,#4b4860 75%,#2e2c35 100%)}
.slide-label{position:absolute;left:80px;top:214px;color:#fff;font-family:"PT Sans Narrow",sans-serif;font-weight:700;font-size:14px;letter-spacing:3px}
.caption{position:absolute;left:0;right:0;bottom:0;height:50px;background:rgba(0,0,0,.65);color:#fff;font-family:"PT Sans Narrow",sans-serif;font-weight:700;font-size:11px;line-height:17px;padding:8px 14px}
.intro{left:486px;top:511px;width:497px;height:97px;background:var(--panel);border:1px solid #d5e0ec;text-align:center;font-family:"PT Sans Narrow",sans-serif;color:var(--ink)}
.intro h2{font-size:17px;font-weight:700;margin-top:12px}
.intro p{font-style:italic;font-weight:700;font-size:11px;line-height:19px;color:#111;margin-top:12px}
.card{top:631px;width:161px;height:190px;border:1px solid var(--line);padding:10px 13px}
.card h3{text-align:center;font-size:11px;color:var(--ink);font-weight:700;margin-bottom:14px}
.card p{font-size:9.5px;line-height:12.3px;letter-spacing:1px;text-align:justify;color:#444}
.card .more{position:absolute;bottom:10px;left:0;right:0;text-align:center;font-size:10px;color:var(--gold)}
.foot{color:var(--white);font-size:12px;line-height:21px}
.foot h4{font-size:11.5px;font-weight:700;margin-bottom:9px}
.foot .socials{padding:0;gap:10px}
.copy{left:202px;top:941px;width:795px;height:26px;background:var(--white);text-align:center;font-size:10px;color:#777;line-height:26px}
</style>
</head>
<body>
<nav class="abs nav">
  <a class="active">Home</a><a>Calendar</a><a>About Us</a><a>Donate</a><a>Travel Information</a><a>Contact</a>
</nav>

<header class="abs masthead">
  <div class="brand-mark"></div>
  <div class="brand-name">Tidewater Dialogues</div>
</header>

<aside class="abs sidebar">
  <div class="band">Join Us / Follow Us</div>
  <div class="socials"><div class="sq fb"></div><div class="sq yt"></div><div class="sq tw"></div></div>
  <div class="band">Join Our Mailing List</div>
  <div class="mail"><div class="field"></div><div class="join">JOIN</div></div>
  <div class="band">Upcoming Events</div>

  <div class="event" style="top:229px">
    <div class="headshot" style="top:0"><div role="img" aria-label="Presenter headshot" style="background:linear-gradient(160deg,#d8b27a,#b7825a 60%,#7c5a40)"></div></div>
    <div class="meta">June 1, 2013<br>Starting Close In<br>Presenters: Daniel<br>and Margaret Holloway</div>
    <div class="lead" style="top:73px">Heeding the implicit wisdom in E.R. Whitcombe's line "We had the ex</div>
    <div class="rest" style="top:128px">perience but missed the meaning," this concluding workshop is designed to help us capture all the gold coins that we tucked in our pockets for later contemplation. We will encourage participants to identify and name the excitements, the questions and challenges that have stirred us like</div>
  </div>

  <div class="event" style="top:454px">
    <div class="headshot" style="top:0;left:2px"><div role="img" aria-label="Presenter headshot" style="background:linear-gradient(160deg,#8a6a58,#b98a70 50%,#5e4a44)"></div></div>
    <div class="meta">June 1, 2013<br>Starting Close In<br>Presenters: Daniel<br>and Margaret Holloway</div>
    <div class="lead" style="top:70px">Heeding the implicit wisdom in E.R. Whitcombe's line "We had the ex</div>
    <div class="rest" style="top:132px">perience but missed the meaning," this concluding workshop is designed to help us capture all the gold coins that we tucked in our pockets for later contemplation. We will encourage participants to identify and name the excitements, the questions and challenges that have stirred us like</div>
  </div>
</aside>

<main class="abs main"></main>

<section class="abs slide" role="img" aria-label="Slideshow photo of a historic harbour town street at dusk">
  <div class="slide-label">SLIDESHOW</div>
  <div class="caption">Tidewater Dialogues is bringing together speakers from around the globe who are transforming<br>our world. Join us for an event that could change your life.</div>
</section>

<section class="abs intro">
  <h2>Conversations that Could Transform your Life</h2>
  <p>Tidewater Dialogues is bringing together speakers from around the globe who are transforming<br>our world. Join us for an event that could change your life.</p>
</section>

<article class="abs card" style="left:486px">
  <h3>ABOUT US</h3>
  <p>Tidewater Dialogues Inc. is a non-profit 501©3 educational and service organization, grounded in the recognition that active engagement of the arts through can be an entry into growth and transformation.</p>
  <div class="more">Read more</div>
</article>
<article class="abs card" style="left:653px">
  <h3>OUR SPEAKERS</h3>
  <p>Our speakers are Lorem ipsum dolor sit amet, consectetur adipisicing elit, sed do eiusmod tempor incididunt ut labore et dolore magna aliqua. Ut enim ad minim veniam, quis n</p>
  <div class="more">Read more</div>
</article>
<article class="abs card" style="left:821px">
  <h3>ANNAPOLIS</h3>
  <p>Annapolis, MD is Lorem ipsum dolor sit amet, consectetur adipisicing elit, sed do eiusmod tempor incididunt ut labore et dolore magna aliqua. Ut enim ad minim veniam, quis n</p>
  <div class="more">Read more</div>
</article>

<footer>
  <div class="abs foot" style="left:202px;top:858px">
    <h4>Links</h4>
    <div>Home | Calendar | About Us | Donate</div>
    <div>Travel Information | Contact</div>
  </div>
  <div class="abs foot" style="left:542px;top:858px">
    <h4>Contact Us</h4>
    <div style="line-height:17px">Address, Phone Number,<br>Email etc.</div>
  </div>
  <div class="abs foot" style="left:861px;top:858px">
    <h4>Follow Us</h4>
    <div class="socials"><div class="sq fb"></div><div class="sq yt"></div><div class="sq tw"></div></div>
  </div>
  <div class="abs copy">Copyright Tidewater Dialogues. All rights reserved.</div>
</footer>
</body>
</html>
```